Accountability Project Graphics

I want to create 10 social media graphics (new Instagram size 4:5 (1080 x 1350 pixels) focusing on our Kelmora Accountability App, using any of the 3 pictures attached. Use the attached pics only, NO RANDOM STOCK PHOTOGRAPHY. For the color scheme, use the landing page colors/fonts (attached).
You can add any of the 3 photos attached but I mainly need BOLD text that includes these headlines and sub-headlines on them.
Please NOTE for all the headlines below, also add this sub-headline on each graphic:
Stay Consistent with MB in Your Pocket!
Here are the headlines:
• Stop Starting Over Every Monday
• You don't need more willpower. You need more support
• Built for women who are tired of doing this alone
• When Motivation Fades, MB Checks In
• The Support System You've Been Missing
• Support When Motivation Disappears
• What if MB Checked in Every Day?
• The Missing Piece Isn't Another Diet
• Eat the food you love. Stay accountable every day.
• One Bad Meal Doesn't Mean You Failed
women over 40 trying to lose weight

```html
<!DOCTYPE html>
<html lang="en">
<head>
<meta charset="utf-8">
<title>Kelmora Accountability Graphics</title>
<link href="https://fonts.googleapis.com/css2?family=Fraunces:ital,opsz,wght@0,9..144,600;0,9..144,800;1,9..144,600;1,9..144,800&family=Inter:wght@600;700&display=swap" rel="stylesheet">
<style>
:root{
  --board:#555555;
  --blush:#fde6ec;
  --blush-light:#fdf0f3;
  --blush-deep:#f9d4de;
  --plum:#2e1a3f;
  --rose:#d2527f;
  --photo-warm:#c9a99a;
  --photo-dark:#3a2d3c;
  --photo-denim:#4e5f7c;
  --photo-light:#e9e4e4;
  --photo-lilac:#cdb6e2;
}
*{margin:0;padding:0;box-sizing:border-box}
html,body{width:1200px;height:751px;overflow:hidden;background:var(--board)}
.board{position:relative;width:1200px;height:751px}
.post{position:absolute;overflow:hidden;background:linear-gradient(180deg,#fdeef1 0%,var(--blush) 55%,var(--blush-deep) 100%);font-family:"Fraunces",Georgia,serif;font-variation-settings:"opsz" 36;color:var(--plum)}
.post *{position:absolute;line-height:1;white-space:nowrap}
.hero{left:45px;top:38px;width:540px;height:676px}
.small{width:170px;height:213px}
.c1{left:609px}.c2{left:805px}.c3{left:995px}
.r1{top:38px}.r2{top:270px}.r3{top:498px}
.serif{font-weight:800}
.ital{font-style:italic;font-weight:800}
.rose{color:var(--rose)}
.tag{font-family:"Inter",Arial,sans-serif;font-weight:700;font-size:7px;line-height:1.3;color:var(--plum)}
.tag span{position:static;color:var(--rose)}
.halo{border-radius:50%;background:var(--blush-light)}
.photo-solo{background:linear-gradient(180deg,var(--photo-warm) 0%,var(--photo-warm) 12%,var(--photo-dark) 38%,var(--photo-dark) 100%)}
.photo-duo{background:linear-gradient(90deg,var(--photo-denim) 0%,var(--photo-light) 40%,var(--photo-light) 55%,var(--photo-denim) 75%,var(--photo-dark) 100%)}
.photo-hug{background:linear-gradient(135deg,var(--photo-lilac) 0%,#6b5a7a 40%,#e2708f 70%,var(--blush) 100%)}
.fade-left{-webkit-mask-image:linear-gradient(90deg,transparent 0%,#000 30%);mask-image:linear-gradient(90deg,transparent 0%,#000 30%)}
.fade-right{-webkit-mask-image:linear-gradient(270deg,transparent 0%,#000 30%);mask-image:linear-gradient(270deg,transparent 0%,#000 30%)}
.fade-down{-webkit-mask-image:linear-gradient(180deg,#000 65%,transparent);mask-image:linear-gradient(180deg,#000 65%,transparent)}
</style>
</head>
<body>
<main class="board">

  <section class="post hero">
    <div class="halo" style="left:193px;top:292px;width:520px;height:520px"></div>
    <div class="photo-solo" role="img" aria-label="Smiling coach in black lace top, hand on hip" style="left:300px;top:235px;width:240px;height:441px;border-radius:110px 110px 0 0"></div>
    <h1 class="serif" style="left:34px;top:18px;font-size:112px">Stop</h1>
    <div class="ital" style="left:28px;top:124px;font-size:104px;letter-spacing:-2px">Starting</div>
    <div class="serif" style="left:30px;top:238px;font-size:60px">Over</div>
    <div class="serif rose" style="left:30px;top:298px;font-size:60px">Every</div>
    <div class="serif rose" style="left:30px;top:358px;font-size:60px">Monday</div>
    <p class="tag" style="left:30px;top:590px;font-size:20px">Stay Consistent with<br><span>MB in Your Pocket!</span></p>
  </section>

  <section class="post small c1 r1">
    <div class="photo-duo fade-left" role="img" aria-label="Two women laughing together in denim" style="left:64px;top:61px;width:106px;height:152px"></div>
    <div class="serif rose" style="left:0;width:170px;text-align:center;top:8px;font-size:18px">Built for</div>
    <div class="ital rose" style="left:0;width:170px;text-align:center;top:24px;font-size:32px">women</div>
    <div class="serif" style="left:9px;top:66px;font-size:12.5px;line-height:16px">who are<br>tired of<br>doing<br>this<br>alone</div>
    <p class="tag" style="left:9px;top:168px;font-size:6.5px">Stay<br>Consistent<br><span>with MB in Your<br>Pocket!</span></p>
  </section>

  <section class="post small c2 r1">
    <div class="photo-solo fade-left" role="img" aria-label="Coach in black lace top smiling" style="left:80px;top:0;width:90px;height:213px"></div>
    <div class="serif" style="left:11px;top:22px;font-size:14px">One</div>
    <div class="serif" style="left:11px;top:40px;font-size:14px">Bad Meal</div>
    <div class="ital rose" style="left:9px;top:59px;font-size:20px;line-height:23px">Doesn't<br>Mean</div>
    <div class="ital" style="left:9px;top:110px;font-size:26px;line-height:27px">You<br>Failed</div>
    <p class="tag" style="left:11px;top:185px">Stay Consistent with<br><span>MB in Your Pocket!</span></p>
  </section>

  <section class="post small c3 r1">
    <div class="photo-duo fade-right" role="img" aria-label="Coach and friend laughing side by side" style="left:0;top:92px;width:104px;height:121px"></div>
    <div class="ital" style="left:68px;top:14px;font-size:13px">Eat the</div>
    <div class="ital" style="left:8px;top:18px;font-size:48px;letter-spacing:-1px">food</div>
    <div class="ital rose" style="right:9px;top:64px;font-size:23px">you love</div>
    <div class="ital" style="right:9px;top:101px;font-size:9px;line-height:10px;text-align:right">Stay<br>accountable</div>
    <div class="ital rose" style="right:9px;top:119px;font-size:17px;line-height:18px;text-align:right">every<br>day.</div>
    <p class="tag" style="right:9px;top:168px;text-align:right">Stay<br>Consistent<br><span>with MB in Your<br>Pocket!</span></p>
  </section>

  <section class="post small c1 r2">
    <div class="photo-hug fade-down" role="img" aria-label="Coach hugging a laughing client in a store" style="left:0;top:0;width:170px;height:120px"></div>
    <div class="ital" style="left:17px;top:96px;font-size:13px">The</div>
    <div class="ital rose" style="left:12px;top:108px;font-size:33px">Missing</div>
    <div class="ital" style="left:11px;top:145px;font-size:36px">Piece</div>
    <div class="ital" style="left:126px;top:157px;font-size:8px;line-height:8.5px">isn't<br>another<br>diet</div>
    <p class="tag" style="left:0;width:170px;text-align:center;top:198px">Stay Consistent with <span>MB in Your Pocket!</span></p>
  </section>

  <section class="post small c2 r2">
    <div class="photo-solo fade-left" role="img" aria-label="Coach in black lace top, hand on hip" style="left:77px;top:65px;width:93px;height:148px"></div>
    <div class="ital" style="left:11px;top:12px;font-size:12px">What if MB Checked in</div>
    <div class="serif rose" style="left:10px;top:28px;font-size:38px;letter-spacing:-1px">EVERY</div>
    <div class="serif rose" style="left:12px;top:70px;font-size:28px">Day?</div>
    <p class="tag" style="left:13px;top:173px">Stay<br>Consistent with<br><span>MB in Your Pocket!</span></p>
  </section>

  <section class="post small c3 r2">
    <div class="photo-hug fade-left" role="img" aria-label="Faded photo of coach embracing a laughing client" style="left:60px;top:0;width:110px;height:213px;opacity:.45"></div>
    <div class="ital" style="left:11px;top:10px;font-size:19px;line-height:22px">The<br>Support<br>System</div>
    <div class="serif rose" style="left:11px;top:84px;font-size:25px;line-height:27px">You've<br>Been<br>Missing</div>
    <p class="tag" style="left:12px;top:183px">Stay Consistent with<br><span>MB in Your Pocket!</span></p>
  </section>

  <section class="post small c1 r3">
    <div class="photo-solo fade-down" role="img" aria-label="Coach in black lace top smiling" style="left:77px;top:0;width:93px;height:120px"></div>
    <div class="ital" style="left:15px;top:70px;font-size:25px">When</div>
    <div class="ital" style="left:12px;top:95px;font-size:25px;letter-spacing:-.5px">Motivation</div>
    <div class="serif rose" style="left:11px;top:122px;font-size:40px;letter-spacing:-.5px">FADES</div>
    <div class="ital" style="right:12px;top:165px;font-size:10px">MB Checks In</div>
    <p class="tag" style="left:0;width:170px;text-align:center;top:188px">Stay Consistent with<br><span>MB in Your Pocket!</span></p>
  </section>

  <section class="post small c2 r3">
    <div class="photo-duo fade-left" role="img" aria-label="Coach and friend standing together laughing" style="left:55px;top:98px;width:115px;height:115px"></div>
    <div class="serif" style="left:-79px;top:86px;width:210px;height:44px;font-size:44px;text-align:center;transform:rotate(-90deg);transform-origin:center">Support</div>
    <div class="ital" style="left:70px;top:12px;font-size:15px">When</div>
    <div class="ital rose" style="left:69px;top:30px;font-size:14.5px;line-height:20px">Motivation<br>Disappears</div>
    <p class="tag" style="left:69px;top:76px">Stay Consistent with<br><span>MB in Your Pocket!</span></p>
  </section>

  <section class="post small c3 r3">
    <div class="photo-hug fade-down" role="img" aria-label="Coach hugging a laughing client in a store" style="left:0;top:0;width:170px;height:110px"></div>
    <div class="serif" style="left:0;width:170px;text-align:center;top:102px;font-size:11px;line-height:12.5px;font-weight:600">You don't need<br>more willpower.</div>
    <div class="serif rose" style="left:0;width:170px;text-align:center;top:130px;font-size:10px;font-weight:600">You need</div>
    <div class="ital rose" style="left:0;width:170px;text-align:center;top:138px;font-size:30px">more</div>
    <div class="ital rose" style="left:0;width:170px;text-align:center;top:162px;font-size:28px">support</div>
    <p class="tag" style="left:0;width:170px;text-align:center;top:200px;font-size:6.5px">Stay Consistent with <span>MB in Your Pocket!</span></p>
  </section>

</main>
</body>
</html>
```